Property Management business needs Business cards designed

We provide a premium property management service based in Sydney's Norther Beaches. We want people to feel confident in choosing us to manage their investment properties. We offer a much more personalized service than other estate agents.
We want a modern clean design. Something that shows confidence without being complicated.
Logo attached.

Target Market(s)

35-70yo Male and Female with strong property portfolios within Sydney's Norther Beaches

Industry/Entity Type

Property Management

Contact Information for Business Card

Address: Suite 7, 12-14 Kelvin Parade, Harlow NSW 2188
Two separate named cards.
Tom Ardley - 0491 570 118 tom@harbourvaleestates.com.au
Clara Dunmore - 0491 570 263 clara@harbourvaleestates.com.au

Requirements
Must have
• Business logo, name, number, address, email.

```html
<!DOCTYPE html>
<html lang="en">
<head>
<meta charset="utf-8">
<title>Harbourvale Estates – Business Card</title>
<link rel="stylesheet" href="https://fonts.googleapis.com/css2?family=Open+Sans:wght@400;600;700&display=swap">
<style>
  :root {
    --backdrop: #8f8f8f;
    --card-light: #f1f1f2;
    --card-dark: #0f1416;
    --teal: #1b7d8c;
    --teal-bright: #2a9aa6;
    --ink: #1b1b1b;
    --ink-soft: #3a3a3a;
    --paper-text: #e6e8ea;
  }
  * { box-sizing: border-box; margin: 0; padding: 0; }
  html, body {
    width: 1105px;
    height: 1200px;
    overflow: hidden;
    background: var(--backdrop);
    font-family: "Open Sans", Arial, sans-serif;
  }
  .sheet {
    position: relative;
    width: 1105px;
    height: 1200px;
  }
  .card {
    position: absolute;
    left: 182px;
    width: 747px;
    height: 427px;
  }
  .card--front { top: 119px; background: var(--card-light); }
  .card--back  { top: 637px; background: var(--card-dark); }

  /* Front */
  .brand {
    position: absolute;
    right: 41px;
    top: 82px;
    display: flex;
    align-items: center;
    gap: 12px;
  }
  .brand__mark {
    width: 18px;
    height: 18px;
    border-radius: 50%;
    background: var(--teal);
  }
  .brand__name {
    font-weight: 700;
    font-size: 31px;
    letter-spacing: -0.3px;
    color: var(--ink);
    line-height: 1;
  }
  .holder {
    position: absolute;
    left: 40px;
    top: 243px;
    font-weight: 600;
    font-size: 27px;
    color: var(--teal);
    line-height: 1.2;
  }
  .rule {
    position: absolute;
    left: 40px;
    right: 41px;
    top: 287px;
    height: 1.5px;
    background: var(--teal);
  }
  .contacts {
    position: absolute;
    left: 44px;
    top: 302px;
    list-style: none;
  }
  .contacts li {
    display: flex;
    align-items: center;
    gap: 8px;
    height: 29px;
    font-size: 19px;
    color: var(--ink-soft);
  }
  .contacts svg { width: 17px; height: 17px; flex: none; }
  .address {
    position: absolute;
    right: 41px;
    top: 302px;
    text-align: right;
    font-style: normal;
    font-size: 19px;
    line-height: 29px;
    color: var(--ink-soft);
  }

  /* Back */
  .back-brand {
    position: absolute;
    left: 0;
    right: 0;
    top: 196px;
    display: flex;
    justify-content: center;
    align-items: center;
    gap: 16px;
  }
  .back-brand__mark {
    width: 26px;
    height: 26px;
    border-radius: 50%;
    background: var(--teal-bright);
  }
  .back-brand__name {
    font-weight: 700;
    font-size: 40px;
    color: var(--paper-text);
    line-height: 1;
  }
  .web {
    position: absolute;
    left: 0;
    right: 0;
    top: 362px;
    text-align: center;
    font-size: 21px;
    letter-spacing: 5.2px;
    color: var(--paper-text);
  }
</style>
</head>
<body>
<main class="sheet">
  <section class="card card--front" aria-label="Card front">
    <div class="brand">
      <span class="brand__mark"></span>
      <span class="brand__name">HARBOURVALE ESTATES</span>
    </div>

    <h1 class="holder">Tom Ardley</h1>
    <div class="rule"></div>

    <ul class="contacts">
      <li>
        <svg viewBox="0 0 24 24" aria-hidden="true"><path fill="#1b7d8c" d="M6.6 10.8a15.2 15.2 0 0 0 6.6 6.6l2.2-2.2a1 1 0 0 1 1-.25 11.4 11.4 0 0 0 3.6.57 1 1 0 0 1 1 1V20a1 1 0 0 1-1 1A17 17 0 0 1 3 4a1 1 0 0 1 1-1h3.5a1 1 0 0 1 1 1c0 1.25.2 2.45.57 3.57a1 1 0 0 1-.25 1z"/></svg>
        0491 570 118
      </li>
      <li>
        <svg viewBox="0 0 24 24" aria-hidden="true"><rect x="2" y="5" width="20" height="14" rx="1.5" fill="#1b7d8c"/><path d="M3 6.5l9 6.5 9-6.5" fill="none" stroke="#f1f1f2" stroke-width="1.6"/></svg>
        tom@harbourvaleestates.com.au
      </li>
      <li>
        <svg viewBox="0 0 24 24" aria-hidden="true"><circle cx="12" cy="12" r="10" fill="#1b7d8c"/><path d="M2 12h20M12 2c3 3 3 17 0 20M12 2c-3 3-3 17 0 20" fill="none" stroke="#f1f1f2" stroke-width="1.3"/></svg>
        www.harbourvaleestates.com.au
      </li>
    </ul>

    <address class="address">
      Suite 7<br>
      12-14 Kelvin Parade<br>
      Harlow NSW 2188
    </address>
  </section>

  <section class="card card--back" aria-label="Card back">
    <div class="back-brand">
      <span class="back-brand__mark"></span>
      <span class="back-brand__name">HARBOURVALE ESTATES</span>
    </div>
    <p class="web">www.harbourvaleestates.com.au</p>
  </section>
</main>
</body>
</html>
```